Graphic design

We are looking for a graphic design for a trade show banner. The banner will be 10 feet x 10 feet. We are an adventure based tour operator in Costa Rica. The graphic should inspire a sense of adventure as well as being clear and not too cluttered. Our website is www.verdalunatrek.com

The following text should be used on the banner:

1. Our Logo (attached)
2. 8 Days. 8 Adventures. 1 Life
3. Summit Chase Circuit (name of the tour we are selling). The "Summit Chase Circuit" wording should be prominent. Underneath, or somewhere close to that wording there should be, in smaller text, "All inclusive Costa Rica Adventure Tour"
4. Price $1799 with a slash through it and then special promotion price of $1449. Text should read "Book this weekend and save $350!"
5. Meridian Horizon Logo (Attached)
6. "Rafting, ziplining, kayaking, surfing, snorkeling, wildlife, jungle lodge, waterfall rappelling, hiking, mountain biking"
7. www.VerdaLunaTrek.com

We have attached some pictures. Not all need to be used but the rafting photo definitely needs to be used.

Industry/Entity Type

Graphic Design

Colors
33a6d7
3276b5
0355a3

```html
<!DOCTYPE html>
<html lang="en">
<head>
<meta charset="utf-8">
<title>Summit Chase Circuit – Verda Luna Trek</title>
<link rel="stylesheet" href="https://fonts.googleapis.com/css2?family=Arimo:wght@400;700&display=swap">
<style>
  :root {
    --blue-deep: #0355a3;
    --blue-mid: #3276b5;
    --blue-light: #33a6d7;
    --blue-band: #2f93cc;
    --orange: #f39c1e;
    --orange-hot: #f26522;
    --tag-paper: #f1e6cf;
    --price-red: #e4572e;
    --string: #b58a4a;
    --white: #ffffff;
    --jungle: #3f6b2c;
  }
  html, body { margin: 0; padding: 0; overflow: hidden; background: var(--white); }
  .banner {
    position: relative;
    width: 1200px;
    height: 1200px;
    overflow: hidden;
    background: linear-gradient(180deg, var(--blue-deep) 0%, var(--blue-mid) 55%, var(--blue-deep) 100%);
    font-family: "Arimo", Arial, sans-serif;
    color: var(--white);
  }
  .brand {
    position: absolute;
    left: 74px;
    top: 72px;
    display: flex;
    align-items: center;
    gap: 18px;
  }
  .brand-name {
    font-weight: 400;
    font-size: 54px;
    letter-spacing: 4px;
    color: var(--orange);
    line-height: 1;
  }
  .brand-dot {
    width: 42px; height: 42px; border-radius: 50%;
    background: var(--blue-light);
  }
  .award-badge {
    position: absolute; left: 1000px; top: 32px; width: 148px; height: 191px;
    background: #111;
  }
  .tagline {
    position: absolute; left: 84px; top: 202px; margin: 0;
    font-size: 26px; font-weight: 700; line-height: 32px;
  }
  .headline {
    position: absolute; left: 74px; top: 254px; margin: 0;
    font-family: "Arimo", Arial, sans-serif;
    font-size: 82px; font-weight: 700; line-height: 96px;
    letter-spacing: -0.5px;
  }
  .subhead-band {
    position: absolute; left: 0; top: 355px; width: 1200px; height: 65px;
    background: var(--orange);
    display: flex; align-items: center;
  }
  .subhead {
    margin: 0 0 0 78px;
    font-size: 29px; font-weight: 700;
    letter-spacing: 2px; color: var(--blue-deep);
  }
  .photo { position: absolute; }
  .photo-zipline {
    left: 0; top: 420px; width: 300px; height: 558px;
    background: linear-gradient(160deg, #2f5a22 0%, #5f8f3a 50%, #9a8a6a 100%);
  }
  .photo-rafting {
    left: 310px; top: 420px; width: 890px; height: 558px;
    background: linear-gradient(180deg, var(--jungle) 0%, #7d8a6a 40%, #c9d7df 70%, var(--blue-light) 100%);
  }
  .activities-band {
    position: absolute; left: 288px; top: 978px; width: 912px; height: 156px;
    background: var(--blue-band);
  }
  .activities {
    position: absolute; left: 300px; top: 993px; width: 580px; margin: 0;
    font-size: 22px; font-weight: 700; line-height: 42px; color: var(--white);
  }
  .photo-guide {
    left: 876px; top: 654px; width: 324px; height: 546px;
    background: linear-gradient(180deg, #4a4f52 0%, #c99b7c 45%, #e6c2a8 100%);
    border-top-left-radius: 140px;
  }
  .price-tag {
    position: absolute; left: 870px; top: 230px; width: 330px; height: 500px;
  }
  .save-tag {
    position: absolute; left: 0; top: 850px; width: 300px; height: 280px;
  }
  .save-text {
    position: absolute; left: 30px; top: 871px; width: 240px;
    text-align: center; color: var(--white); font-weight: 700;
  }
  .save-text .small { display: block; font-size: 25px; line-height: 58px; }
  .save-text .big { display: block; font-size: 38px; line-height: 54px; }
  .footer-band {
    position: absolute; left: 0; top: 1134px; width: 1200px; height: 66px;
    background: var(--blue-deep);
  }
  .website {
    position: absolute; left: 0; top: 1134px; width: 908px; height: 66px; margin: 0;
    display: flex; align-items: center; justify-content: center;
    font-size: 24px; font-weight: 700;
  }
</style>
</head>
<body>
<div class="banner">
  <div class="brand">
    <span class="brand-name">VERDA LUNA TREK</span>
    <span class="brand-dot"></span>
  </div>
  <div class="award-badge" role="img" aria-label="Meridian Horizon award badge"></div>

  <p class="tagline">8 Days. 8 Adventures. 1 Life</p>
  <h1 class="headline">Summit Chase Circuit</h1>

  <div class="subhead-band"><p class="subhead">All inclusive Costa Rica Adventure Tour</p></div>

  <div class="photo photo-zipline" role="img" aria-label="Woman in helmet and harness riding a zipline through the jungle"></div>
  <div class="photo photo-rafting" role="img" aria-label="Group of rafters in helmets and life vests cheering with paddles raised in whitewater"></div>

  <div class="activities-band"></div>
  <p class="activities">Rafting, Ziplining, Kayaking, Surfing, Snorkeling, Wildlife, Jungle lodge, Waterfall rappelling, Hiking, Mountain biking</p>

  <div class="photo photo-guide" role="img" aria-label="Smiling tour guide wearing a cap"></div>

  <svg class="price-tag" viewBox="0 0 330 500" aria-label="Special promotion price, was $1799, now $1449">
    <path d="M150 128 Q200 20 330 50" fill="none" stroke="var(--string)" stroke-width="3"/>
    <g transform="rotate(15 165 290)">
      <rect x="40" y="140" width="250" height="300" fill="var(--tag-paper)"/>
      <rect x="40" y="140" width="250" height="125" fill="var(--blue-light)"/>
      <circle cx="165" cy="170" r="12" fill="var(--blue-mid)" stroke="var(--tag-paper)" stroke-width="5"/>
      <text x="165" y="222" text-anchor="middle" font-family="Arimo, sans-serif" font-weight="700" font-size="21" fill="var(--tag-paper)">SPECIAL PROMOTION</text>
      <text x="165" y="249" text-anchor="middle" font-family="Arimo, sans-serif" font-weight="700" font-size="21" fill="var(--tag-paper)">PRICE</text>
      <text x="165" y="310" text-anchor="middle" font-family="Arimo, sans-serif" font-weight="700" font-size="38" fill="var(--price-red)">$1799</text>
      <line x1="92" y1="297" x2="238" y2="297" stroke="var(--price-red)" stroke-width="4"/>
      <text x="165" y="385" text-anchor="middle" font-family="Arimo, sans-serif" font-weight="700" font-size="66" fill="var(--price-red)">$1449</text>
    </g>
  </svg>

  <svg class="save-tag" viewBox="0 0 300 280" aria-hidden="true">
    <path d="M-20 138 L70 45 A128 128 0 1 1 70 231 Z" fill="var(--orange-hot)" stroke="var(--white)" stroke-width="4"/>
    <circle cx="20" cy="138" r="11" fill="var(--blue-mid)"/>
  </svg>
  <div class="save-text">
    <span class="small">Book this</span>
    <span class="small">weekend</span>
    <span class="big">save</span>
    <span class="big">$350!</span>
  </div>

  <div class="footer-band"></div>
  <p class="website">www.VerdaLunaTrek.com</p>
</div>
</body>
</html>
```